BrightFern Web Design Project

BrightFern IT solutions, a IT mananaged services company is looking to redesign current website (brightfernsolutions.example).

The website should convey professionalism within the managed it services community. The layout should invite users to explore other areas of the site. Should contain tools and other current information that clients or potential clients would find useful. Product pages, special offers and informational pages should be easily editable by non-programmers. Tidewarden.example is a good site to review as an example of the design components we like.

Target Market(s)

Professional services companies with 10-100 users

Industry/Entity Type

It Company

Requirements
Must have
• • Clickable icons and graphics are good
• SEO - Wordpress could be a great platform for us to work from as we already have internal experience with it and it’s easy to update. If not Wordpress, we would need something that is easy to SEO optimize
• An “our team” section with pictures
• Sell the message to potential clients why they need managed services
• Home page needs to convey our core services at a glance
• Home page needs to load quickly
• Screenshots of our monitoring and security reports
• Easy for us to update/edit certain areas
o New products
o Testimonials
Nice to have
• • Something like TW’s savings calculator - http://www.tidewarden.example/it-savings-calculator/
• Webform to enter service ticket requests
• Motion of home page banner
• Maybe pull in RSS feeds from current tech news sources
• Rotating content on all pages to keep it fresh
• “Fern-up” feature for monthly promos
Should not have
• • Should not be overly "techie" in feel.
• Not overly wordy (like current site)

```html
<!DOCTYPE html>
<html lang="en">
<head>
<meta charset="utf-8">
<title>BrightFern IT Solutions</title>
<link rel="stylesheet" href="https://fonts.googleapis.com/css2?family=PT+Sans:ital,wght@0,400;0,700;1,400&family=Cambo&display=swap">
<style>
:root{
  --page:#f3f0f0;
  --header:#f6f4f4;
  --green:#8fd13a;
  --green-deep:#5fa82a;
  --panel:#6c8a4e;
  --panel-dark:#4f6c38;
  --nav-dark:#2d2d24;
  --nav-home:#9bd032;
  --heading-blue:#1f6f9c;
  --body-grey:#9a9a9a;
  --col-text:#555;
  --orange:#f0a060;
  --arrow-blue:#3f6f93;
  --arrow-grey:#b9bfc3;
  --frame:#d9d9d9;
}
*{box-sizing:border-box;margin:0;padding:0}
html,body{width:1002px;height:1200px;overflow:hidden;background:var(--page)}
body{position:relative;font-family:"PT Sans",sans-serif}
.abs{position:absolute}

.site-header{left:0;top:0;width:1002px;height:81px;background:linear-gradient(#ffffff,var(--header))}
.brand{left:94px;top:8px;width:100px;height:70px;text-align:center}
.brand-dot{display:block;margin:0 auto 4px;width:40px;height:40px;border-radius:50%;background:var(--green-deep)}
.brand-name{font-size:17px;color:var(--green-deep);font-weight:400}
.call-label{left:573px;top:8px;font-size:15px;color:#222}
.call-number{left:573px;top:23px;font-family:"Cambo",serif;font-size:23px;color:#222}
.main-nav a{position:absolute;top:55px;height:21px;border-radius:3px;background:var(--nav-dark);color:#fff;font-size:14px;line-height:21px;text-align:center;text-decoration:none}
.main-nav a.current{background:var(--nav-home)}

.hero{left:0;top:81px;width:1002px;height:245px;background:radial-gradient(ellipse at 50% 40%,#a8e05a,var(--green) 55%,var(--green-deep))}
.hero-slide{left:199px;top:104px;width:647px;height:207px;background:linear-gradient(90deg,var(--panel),#7f9d5f 50%,var(--panel-dark));border:2px solid #b4d88a;box-shadow:0 0 10px rgba(0,0,0,.3)}
.hero-photo{left:219px;top:125px;width:151px;height:181px;background:linear-gradient(#e8e0d8,#3a3a3a 70%,#222)}
.hero-title{left:440px;top:140px;width:400px;text-align:center;font-size:28px;color:#fff;letter-spacing:-.5px}
.hero-rule{left:581px;top:180px;width:129px;height:2px;background:var(--orange)}
.hero-text{left:490px;top:191px;width:320px;text-align:center;color:#fff;font-style:italic;font-size:11px;line-height:15.5px}
.arrow{width:32px;height:32px}

.section-title{font-size:16px;color:var(--heading-blue)}
.intro-text{left:108px;width:790px;font-size:11.3px;line-height:17.7px;color:var(--body-grey)}

.portfolio{left:111px;top:603px;width:789px;height:146px;border-radius:6px;background:linear-gradient(#f4f4f4,#d8d8d8);box-shadow:0 1px 3px rgba(0,0,0,.3)}
.thumb{top:612px;width:171px;height:124px;border:1px solid #bbb;border-radius:4px;background:#fff;padding:6px}
.thumb span{display:block;width:100%;height:100%;background:radial-gradient(ellipse at 50% 55%,#4e86c8,#a9c3e0 45%,#fff 75%)}

.service-title{top:796px;font-family:"Cambo",serif;font-size:17px;color:var(--heading-blue);letter-spacing:.3px}
.service-frame{top:838px;width:250px;height:143px;background:#fff;border:1px solid var(--frame);padding:5px;box-shadow:0 -2px 4px rgba(0,0,0,.06)}
.service-frame span{display:block;width:100%;height:100%;background:radial-gradient(ellipse at 50% 50%,#4a7fc4,#b4cbe6 45%,#fff 75%)}
.service-text{top:991px;width:240px;font-size:10.4px;line-height:14px;color:var(--col-text);letter-spacing:.3px}
.learn-more{top:1072px;width:138px;height:26px;border:1px solid #c9c9c9;border-radius:2px;background:linear-gradient(#fafafa,#dcdcdc);font-size:11px;color:#4a6f93;line-height:24px;padding-left:9px}
.learn-more svg{position:absolute;right:10px;top:9px}

.site-footer{left:0;top:1154px;width:1002px;text-align:center;font-family:Arial,sans-serif;font-size:8.5px;line-height:14.5px;color:#000;font-weight:700}
</style>
</head>
<body>

<header class="site-header abs"></header>
<div class="brand abs"><span class="brand-dot"></span><span class="brand-name">BrightFern</span></div>
<div class="call-label abs">Call Us Today</div>
<div class="call-number abs">(888) 555-0142</div>
<nav class="main-nav">
  <a class="current" style="left:565px;width:74px">Home</a>
  <a style="left:646px;width:74px">Solutions</a>
  <a style="left:725px;width:74px">About Us</a>
  <a style="left:803px;width:74px">Careers</a>
  <a style="left:881px;width:74px">Contact</a>
</nav>

<section class="hero abs"></section>
<div class="hero-slide abs"></div>
<div class="hero-photo abs" role="img" aria-label="Businesswoman holding colourful puzzle pieces"></div>
<h1 class="hero-title abs" style="font-weight:400">We Are Leading Solution Provider</h1>
<div class="hero-rule abs"></div>
<p class="hero-text abs">In the information age of today, one must stay abreast of current technology in order to thrive. New advancements are made daily in dispersing information and collaborative computing. High-speed networks aid in the exchange of electronic information between businesses, their customers,s</p>
<svg class="arrow abs" style="left:176px;top:202px" viewBox="0 0 32 32"><circle cx="16" cy="16" r="15" fill="var(--arrow-blue)" stroke="#fff" stroke-width="1.5"/><path d="M19 10 L12 16 L19 22 Z" fill="#fff"/></svg>
<svg class="arrow abs" style="left:838px;top:200px" viewBox="0 0 32 32"><circle cx="16" cy="16" r="15" fill="var(--arrow-blue)" stroke="#fff" stroke-width="1.5"/><path d="M13 10 L20 16 L13 22 Z" fill="#fff"/></svg>

<h2 class="section-title abs" style="left:111px;top:373px;font-weight:400">BrightFern can help your business</h2>
<p class="intro-text abs" style="top:406px">In the information age of today, one must stay abreast of current technology in order to thrive. New advancements are made daily in dispersing information and collaborative computing. High-speed networks aid in the exchange of electronic information between businesses, their customers, vendors, and peers. Businesses that are quick to act and effectively implement this technology will rise to the top.</p>
<p class="intro-text abs" style="top:477px">In the information age of today, one must stay abreast of current technology in order to thrive. New advancements are made daily in dispersing information and collaborative computing. High-speed networks aid in the exchange of electronic information between businesses, their customers, vendors, and peers. Businesses that are quick to act and effectively implement this technology will rise to the top.</p>

<h2 class="section-title abs" style="left:113px;top:558px;font-weight:400">Portfolio</h2>
<div class="portfolio abs"></div>
<div class="thumb abs" style="left:143px"><span role="img" aria-label="Servers connected to laptops"></span></div>
<div class="thumb abs" style="left:326px"><span role="img" aria-label="Figure surrounded by networked desks"></span></div>
<div class="thumb abs" style="left:508px"><span role="img" aria-label="Globe connected to a computer mouse"></span></div>
<div class="thumb abs" style="left:691px"><span role="img" aria-label="Rising blue bar chart blocks"></span></div>
<svg class="arrow abs" style="left:105px;top:661px" viewBox="0 0 32 32"><circle cx="16" cy="16" r="15" fill="var(--arrow-grey)" stroke="#fff" stroke-width="1.5"/><path d="M19 10 L12 16 L19 22 Z" fill="#fff"/></svg>
<svg class="arrow abs" style="left:872px;top:664px" viewBox="0 0 32 32"><circle cx="16" cy="16" r="15" fill="var(--arrow-grey)" stroke="#fff" stroke-width="1.5"/><path d="M13 10 L20 16 L13 22 Z" fill="#fff"/></svg>

<h3 class="service-title abs" style="left:113px;font-weight:400">IT Consulting Services</h3>
<h3 class="service-title abs" style="left:381px;font-weight:400">IT Service Programs</h3>
<h3 class="service-title abs" style="left:649px;font-weight:400">Data Backup and Recovery</h3>

<div class="service-frame abs" style="left:111px"><span role="img" aria-label="Globe connected to a computer mouse"></span></div>
<div class="service-frame abs" style="left:378px"><span role="img" aria-label="Rising blue bar chart blocks"></span></div>
<div class="service-frame abs" style="left:646px"><span role="img" aria-label="Servers connected to laptops"></span></div>

<p class="service-text abs" style="left:115px">Insure that your existing system receives quality service. BrightFern will troubleshoot problems, install new software or parts, and keep your system in optimal condition...</p>
<p class="service-text abs" style="left:383px">The certified professionals at BrightFern will even set up remote access for staff who work outside of the office, but need access to information at their offices...</p>
<p class="service-text abs" style="left:651px">Standalone systems, workstations, network servers, notebooks, peripherals, replacement parts, upgrades, software, Network Design &amp; Installation - BrightFern specializes in all current and legacy network systems...</p>

<div class="learn-more abs" style="left:113px">Learn More<svg width="18" height="7" viewBox="0 0 18 7"><path d="M0 3.5 H15 M12 1 L16 3.5 L12 6" stroke="#7aa6c8" fill="none"/></svg></div>
<div class="learn-more abs" style="left:381px">Learn More<svg width="18" height="7" viewBox="0 0 18 7"><path d="M0 3.5 H15 M12 1 L16 3.5 L12 6" stroke="#7aa6c8" fill="none"/></svg></div>
<div class="learn-more abs" style="left:649px">Learn More<svg width="18" height="7" viewBox="0 0 18 7"><path d="M0 3.5 H15 M12 1 L16 3.5 L12 6" stroke="#7aa6c8" fill="none"/></svg></div>

<footer class="site-footer abs">
  Tidewarden: I.T. Support, Information Technology Services, IT Consulting Experts for Small and Medium Businesses Nationwide<br>
  Tidewarden is a division of BrightFern Solutions Inc.<br>
  All rights reaserved To BrightFern Solutions.
</footer>

</body>
</html>
```